Mobile device purchase and deployment for K-12

Seeking: a great eye, creativity and some good technical sense to design the basic theme, provide the skeleton for a website for a small business. The site functionality should be straightforward with the right wordpress theme and plug-ins; where I really need your expertise is the design and identity, hence the request for logo and business card design for consistent message.

The business: We partner with private schools (mostly K-12, in the future perhaps colleges) to purchase, configure, deploy and manage mobile devices (mainly Tavlets), applications and content (ebooks, courseware, etc.) . Services include helping the schools determine the appropriate technology package (hardware, network, software support, services), help them optimize the financing, and integrate the technology procurement and configuration into the enrollment process. Our solutions are a combination of consulting, financing and technology management.

The users: Two key segments: School administrators and teachers will be interested in the solutions above, with an emphasis on the pedagogical advantages, ease of use and flexibility. Administrators will be interested in the above plus the option of making the solution a source of revenue to the school.

Parents and students will be interested in getting the latest devices, with hardware and software fully configured and supported, at a price comparable or favorable to buying it themselves, with the option for yearly upgrades to the latest technologies. Generally elementary school (a few), middle school (majority), high school. Many parents appreciate knowing that they can implement controls (functionality, apps, hours of usage, age restriction) similar to those of others in the school; others want to customize.

The feel: should be professional but friendly for non-techies; I tend to prefer more abstract and precise to cartoony; however I should acknowledge my own biases which are more technical and quantitative; Basic positioning is making the complex simple for schools and for parents.

Style: Can’t go wrong with Pelorin-inspired design. See http://www.pelorin.com/education/it/ for the type of positioning, strengths, and basic messaging. Note that this is part of campus-based technology offering. Prefer clean, plenty of white space. Ok to contrast with detail when merited (love graphs, charts, creative use of visual display of quantitative info)

Platform: Must be responsive (i.e. look good and have all functionality on desktops, laptops, tablets. Phones would be ideal but understand there may be trade-offs. Strongly prefer Wordpress as a CMS platform because of full range of plug-ins and ability to change hosting providers and themes (minimal lock-in).

info-Architecture: Open to alternatives but here’s current vision for top-level pages: Home/Solutions/About Us/Support. Home is landing page. Solutions describes what we do and describes different options, mainly for administrators and teachers. About us describes the company and has contact info. Support page will be knowledge base and ticketing system, probably by framing a support solution (kelvora or tropane). Footer will have links to terms and conditions, copyright info.

A key functionality will be the ability to add client-organization landing pages. Example: www.sitenamexample.test/schoolname should show a school specific landing page. Initially this will be an order form, with default options selected for that school. Over time, it may become a client portal with log-in and dashboard functionality, downloadable documentation for that school's users.

Logo/identity. I will upload current working draft of logo; feel free to use/adapt/ignore or simply take it as input. Our basic selling point is “mobile education...made simple” which could be a tagline if it works. “Could be “mobility...made simple”. We also talk about "increasing returns to education" based on the concept of "convexity". (More on this below.)

The design element that appealed to me is in the “x” since the name of the service is combination of mobility and convexity, so I like the idea of a curves and lines (like a graph and parabola); convexity technically describes the curve in a type of graph. (Can be looked up for examples, search for convexity - often finance but the idea is increasing returns to scale, so applied to education, "increasing returns to education".)

Target Market(s)

Industry/Entity Type

Education

Contact Information for Business Card

Please see attached business card; note that the mailing address has changed. It is now 17 Birchwell Lane Portsmouth, RI 02871. Other details

Logo Text

Mobility made simple or increasing returns to education - see attachment for current version, feel free to use as input and/or improve on; or come up with something better

Font styles to use
Sans Serif

Requirements
Must have
• Modern, precise feel. I've always been told to stick with reds and blacks plus white, but that may be outdated advice these days.
Nice to have
• Business card should have a QR code that should be non-disruptive, i.e. either small or integrated into design in a creative way. I can generate new QR, willing to use colors or other new approaches.
Should not have
• Avoid cartoonish figures, please. Generally prefer logo types to logos (e.g. KALDO logo or VRN over an abstract image of a computer).

```html
<!DOCTYPE html>
<html lang="en">
<head>
<meta charset="utf-8">
<title>Corvane – Contacts</title>
<link rel="stylesheet" href="https://fonts.googleapis.com/css2?family=Roboto:wght@300;400;500;700&family=Oswald:wght@500&family=Raleway:wght@500&family=Open+Sans:wght@400&display=swap">
<style>
  :root {
    --red: #ef4550;
    --red-dark: #d9303c;
    --ink: #222222;
    --text: #3a3a3a;
    --panel: #f2f2f2;
    --white: #ffffff;
    --line: #9a9a9a;
  }
  * { box-sizing: border-box; margin: 0; padding: 0; }
  html, body { width: 1200px; height: 1162px; overflow: hidden; background: var(--white); }
  body { font-family: "Roboto", sans-serif; color: var(--text); position: relative; }

  .main-nav { position: absolute; left: 0; top: 0; width: 1200px; height: 52px; background: var(--red); }
  .main-nav a { position: absolute; top: 0; height: 52px; line-height: 56px; color: var(--white);
    font-size: 15px; text-decoration: none; transform: translateX(-50%); text-transform: uppercase; }
  .main-nav a.is-active { background: linear-gradient(#3a3a3a, #111); width: 118px; text-align: center; }

  .site-header { position: absolute; top: 52px; left: 0; width: 1200px; height: 111px; }
  .brand { position: absolute; left: 86px; top: 32px; display: flex; align-items: center; gap: 10px; }
  .brand-mark { width: 14px; height: 14px; background: var(--red); }
  .brand-name { font-weight: 700; font-size: 36px; line-height: 40px; color: var(--ink); }
  .login-btn { position: absolute; left: 1014px; top: 37px; width: 99px; height: 41px; border: 1px solid var(--red);
    border-radius: 3px; color: var(--red); font-size: 16px; line-height: 40px; padding-left: 14px; background: var(--white); }
  .login-btn svg { position: absolute; right: 14px; top: 17px; }

  .hero { position: absolute; top: 163px; left: 0; width: 1200px; height: 130px;
    background: linear-gradient(90deg, #6e6a68 0%, #8a8784 30%, #9a9794 55%, #85807c 80%, #a09b97 100%); }
  .hero h1 { position: absolute; width: 100%; top: 36px; text-align: center; font-family: "Oswald", sans-serif;
    font-weight: 500; font-size: 50px; line-height: 56px; color: var(--white); letter-spacing: -0.5px; }

  .contact-card { position: absolute; left: 88px; top: 345px; width: 1023px; height: 480px; background: var(--panel);
    border: 1px solid #e0e0e0; box-shadow: 0 3px 4px rgba(0,0,0,0.18); }
  .section-title { position: absolute; font-weight: 300; font-size: 23px; color: #444; white-space: nowrap; }
  .section-title em { font-style: normal; color: var(--red); }
  .field { position: absolute; left: 71px; width: 442px; background: #fafafa; border: 1px solid var(--line);
    font-size: 14.5px; color: #222; padding-left: 13px; }
  .field-input { height: 49px; line-height: 49px; }
  .field-message { height: 115px; padding-top: 16px; }
  .send-btn { position: absolute; left: 74px; top: 415px; width: 115px; height: 40px; background: var(--red);
    color: var(--white); font-size: 16px; line-height: 40px; text-align: center; }

  .address-block { position: absolute; left: 573px; top: 0; font-family: "Open Sans", sans-serif; }
  .contact-line { position: absolute; left: 0; white-space: nowrap; color: #333; }
  .contact-line svg { position: absolute; left: 0; }
  .contact-name { font-family: "Roboto", sans-serif; font-size: 15px; }
  .contact-name small { color: var(--red); font-size: 11px; }
  .map-area { position: absolute; left: 0; top: 204px; width: 397px; height: 205px;
    background: linear-gradient(135deg, #e4e4e4, #d6d6d6 60%, #e0e0e0); }

  .newsletter { position: absolute; left: 0; top: 895px; width: 1200px; height: 144px; background: #f0515a;
    border-top: 4px solid var(--red-dark); border-bottom: 4px solid var(--red-dark); }
  .newsletter h2 { position: absolute; left: 85px; top: 33px; font-family: "Raleway", sans-serif; font-weight: 500; font-size: 29px; color: var(--white); }
  .newsletter p { position: absolute; left: 85px; top: 74px; width: 430px; font-weight: 500; font-size: 14.5px; line-height: 21px; color: var(--white); }
  .newsletter-input { position: absolute; left: 554px; top: 52px; width: 390px; height: 48px; background: var(--white);
    border: 1px solid #999; font-size: 11.5px; color: #777; line-height: 46px; padding-left: 16px; }
  .subscribe-btn { position: absolute; left: 963px; top: 51px; width: 131px; height: 48px; border-radius: 3px;
    background: linear-gradient(#3a3a3a, #151515); color: var(--white); font-size: 16px; line-height: 48px; text-align: center; }

  .site-footer { position: absolute; top: 1092px; width: 100%; text-align: center; font-size: 16px; color: #333; }
  .site-footer span { margin: 0 6px; }
</style>
</head>
<body>
  <nav class="main-nav">
    <a href="#" style="left:143px">Home</a>
    <a href="#" style="left:286px">Solution</a>
    <a href="#" style="left:431px">About</a>
    <a href="#" class="is-active" style="left:574px">Contact</a>
    <a href="#" style="left:727px">Support</a>
    <a href="#" style="left:872px">Order</a>
    <a href="#" style="left:1026px">Dashboard</a>
  </nav>

  <header class="site-header">
    <div class="brand">
      <span class="brand-mark"></span>
      <span class="brand-name">Corvane</span>
    </div>
    <div class="login-btn">LOGIN
      <svg width="10" height="6" viewBox="0 0 10 6"><path d="M0 0h10L5 6z" fill="var(--red)"/></svg>
    </div>
  </header>

  <section class="hero" role="img" aria-label="Photo of students wearing headphones in a classroom">
    <h1>CONTACTS</h1>
  </section>

  <section class="contact-card">
    <h2 class="section-title" style="left:70px;top:34px">CONTACT US <em>FORM</em></h2>
    <div class="field field-input" style="top:82px">Name</div>
    <div class="field field-input" style="top:149px">Email</div>
    <div class="field field-input" style="top:215px">Phone</div>
    <div class="field field-message" style="top:284px">Message</div>
    <div class="send-btn">SEND</div>

    <div class="address-block">
      <h2 class="section-title" style="left:0;top:34px"><em>ADDRESS</em></h2>
      <div class="contact-line contact-name" style="top:80px">Daniel R.Colby <small>.Director</small></div>
      <div class="contact-line" style="top:106px;font-size:18px;padding-left:28px">
        <svg width="14" height="14" viewBox="0 0 14 14" style="top:6px"><rect width="14" height="14" rx="3" fill="var(--red)"/><path d="M4 3.5c.6 3 2.5 5.5 6.5 7l.5-1.8-2-1-1 .8c-1-.6-1.8-1.4-2.3-2.4l.8-1-1-2z" fill="#fff"/></svg>
        (401)555-0173</div>
      <div class="contact-line" style="top:139px;font-size:14px;padding-left:28px">
        <svg width="15" height="11" viewBox="0 0 15 11" style="top:4px"><rect width="15" height="11" fill="var(--red)"/><path d="M0 0l7.5 6L15 0" fill="none" stroke="#fff" stroke-width="1.2"/></svg>
        daniel.colby@corvane.test</div>
      <div class="contact-line" style="top:167px;font-size:13.5px;padding-left:24px">
        <svg width="10" height="14" viewBox="0 0 10 14" style="top:3px"><path d="M5 0a5 5 0 0 0-5 5c0 3.5 5 9 5 9s5-5.5 5-9a5 5 0 0 0-5-5z" fill="var(--red)"/><circle cx="5" cy="5" r="1.8" fill="#fff"/></svg>
        218 north cedar Ave. #1450 Elmridge, California 90017 USA</div>
      <div class="map-area" role="img" aria-label="Street map showing the office location"></div>
    </div>
  </section>

  <section class="newsletter">
    <h2>Newsletter Subscribers</h2>
    <p>Excepteur sint occaecat cupidatat non proident, sunt in culpa qui officia deserunt mollit anim</p>
    <div class="newsletter-input">Enter your email address</div>
    <div class="subscribe-btn">Subscribers</div>
  </section>

  <footer class="site-footer">Copyright Info<span>|</span>Ownership<span>|</span>Terms and Conditions</footer>
</body>
</html>
```